Flyer for Brivora Water Systems

Flyer to email and leave behind with potential customers. Brivora water systems is the only product available that eliminates scale and prevents it. The system makes scale disappear and prevents scale. Water softeners can only prevent scale but you have to purchase salt and use electricity and also waste water. We will guarantee product for 4 years. No chemicals, all natural, equipment will run longer with no service calls. "Fairy dust"

Target Market(s)

Coffee Equipment, Carwashes, Cooling Towers, Soda Fountain

Industry/Entity Type

Commercial

Font styles to use
Serif
Sans Serif

Colors

Designer to choose colors to be used in the design.

Requirements
Must have
• Professional and clean
Nice to have
• easy read

```html
<!DOCTYPE html>
<html lang="en">
<head>
<meta charset="utf-8">
<title>Brivora Water Systems Flyer</title>
<link href="https://fonts.googleapis.com/css2?family=Roboto+Condensed:wght@300;400;700&family=Raleway:wght@300;400;600;700&family=Montserrat:wght@400;500;600&display=swap" rel="stylesheet">
<style>
  :root{
    --bg:#b4b4b4;
    --paper:#ffffff;
    --blue:#1e88c8;
    --blue-light:#3aa6e6;
    --ink:#2b2b2b;
    --chip:#e6e6e6;
  }
  *{margin:0;padding:0;box-sizing:border-box}
  html,body{width:1200px;height:1200px;overflow:hidden;background:var(--bg)}
  .flyer{position:absolute;left:233px;top:81px;width:734px;height:1038px;background:var(--paper);overflow:hidden;font-family:"Raleway",sans-serif;color:var(--ink)}
  .abs{position:absolute}
  .hero-photo{left:0;top:0;width:359px;height:330px;background:linear-gradient(135deg,#6d6d6d 0%,#a9a9a9 45%,#5a5a5a 100%)}
  .brand-block{left:359px;top:0;width:375px;height:134px;background:linear-gradient(160deg,#2a2a2a,#111)}
  .brand-name{position:absolute;left:0;right:0;top:30px;text-align:center;font-family:"Roboto Condensed",sans-serif;font-weight:700;font-size:44px;letter-spacing:2px;color:var(--blue);line-height:1;white-space:nowrap}
  .brand-rule{position:absolute;left:40px;right:34px;top:96px;height:2px;background:#777}
  .hero-side{left:359px;top:134px;width:375px;height:196px;background:linear-gradient(135deg,#d9d9d9,#ececec 60%,#cfcfcf)}
  .headline{left:404px;top:203px;width:310px;font-family:"Roboto Condensed",sans-serif;font-weight:300;font-size:19.5px;line-height:1.2;color:var(--ink);white-space:nowrap}
  .headline .brand{font-weight:700;font-size:26px;color:var(--blue)}
  .headline strong{display:block;font-weight:700;font-size:22.5px;margin-top:3px}
  h2{font-family:"Roboto Condensed",sans-serif;font-weight:700;font-size:15px;color:var(--blue)}
  h2 span{color:var(--ink)}
  .about-title{left:29px;top:354px}
  .about-text{left:29px;top:380px;width:287px;font-size:12.3px;font-weight:300;line-height:1.22;text-align:justify}
  .about-text p+p{margin-top:8px}
  .proven{left:36px;top:596px;font-family:"Roboto Condensed",sans-serif;font-weight:700;font-size:22px;line-height:1.2;color:#333}
  .proven em{font-style:normal;color:var(--blue-light)}
  .warranty{left:21px;top:669px;width:277px;height:114px;background:#2a2a2a;padding:4px}
  .warranty-inner{width:100%;height:100%;border:2px dotted #fff;text-align:center;font-family:"Roboto Condensed",sans-serif;color:#fff;padding-top:10px}
  .warranty-inner b{display:block;font-size:30px;color:var(--blue-light);line-height:1}
  .warranty-inner p{font-size:13px;line-height:1.25;font-weight:400;margin-top:2px}
  .journey{left:29px;top:807px;width:290px;font-size:12.8px;font-weight:300;line-height:1.3}
  .journey p+p{margin-top:7px}
  .why-title{left:358px;top:354px}
  .perk{display:flex;align-items:center;height:38px;background:var(--chip);font-family:"Montserrat",sans-serif;font-weight:500;font-size:9.8px;line-height:1.25;color:#222;padding-right:4px}
  .perk svg{flex:none;margin-right:6px}
  .perk span{flex:1}
  .perk.wide span{padding-left:10px}
  .results{left:353px;top:761px;width:351px;height:174px;background:#2d2d2d}
  .result{position:absolute;top:13px;width:158px;height:114px;border:2px solid #ddd;background:radial-gradient(circle at 50% 55%,#9a9a95,#5b524b 60%,#7c5a40 100%)}
  .caption{position:absolute;top:138px;width:170px;text-align:center;font-family:"Montserrat",sans-serif;font-size:8.6px;line-height:1.35;color:#eee}
  .footer-dark{left:0;top:984px;width:734px;height:54px;background:#262626}
  .contact-now{left:31px;top:1001px;font-family:"Montserrat",sans-serif;font-weight:600;font-size:11px;color:#fff}
  .phone,.mail{top:998px;font-family:"Montserrat",sans-serif;font-size:13.5px;color:#fff;display:flex;align-items:center;gap:10px}
  .phone{left:216px}
  .mail{left:366px}
  .states{left:556px;top:996px;width:178px;text-align:center;font-family:"Montserrat",sans-serif;font-weight:600;font-size:9px;line-height:1.35;color:#111}
</style>
</head>
<body>
<main class="flyer">
  <div class="abs hero-photo" role="img" aria-label="Black and white photo of industrial water pipes"></div>
  <div class="abs brand-block">
    <div class="brand-name">BRIVORA WATER</div>
    <div class="brand-rule"></div>
  </div>
  <div class="abs hero-side" role="img" aria-label="Faded photo of water system tanks"></div>
  <div class="abs headline"><span class="brand">BRIVORA</span> eliminates scale and<br>prevents water from happening without <strong>CHEMICALS AND ELECTRICITY</strong></div>

  <h2 class="abs about-title">About Us</h2>
  <div class="abs about-text">
    <p>Brivora is the only water system in the world that eliminates scale and prevents it from happening without chemicals and electricity. No need to have multiple filters, Brivora prevents future scale buildup WHILE fixing existing scale problems; all without the introduction of any chemicals into the water supply.</p>
    <p>This is achieved through our patented <b>“fairy-dust”</b>- which is actually a ceramic matrix that encapsulates the Calcium and Magnesium- in layman’s terms it makes the water more slippery at the molecular level!</p>
  </div>

  <div class="abs proven">Proven to last<br><em>4 years+</em> successfully*</div>

  <div class="abs warranty"><div class="warranty-inner">
    <b>4 YEAR WARRANTY</b>
    <p>IF OUR FILTERS/SYSTEMS FAIL TO DO WHAT<br>IS STATED, THE FILTER / SYSTEM WILL BE<br>RE-PLACED OR PURCHASE REFUNDED IN FULL</p>
  </div></div>

  <div class="abs journey">
    <p>To begin your journey to a life free from scale, we kindly need to test your current water hardness, as well as receive your peak water usage numbers (easily obtained from your water bill).</p>
    <p>Chlorine is removed by the carbon filter which has to be changed every six months to maintain the media</p>
  </div>

  <h2 class="abs why-title">Why Brivora is better <span>than water softeners</span></h2>

  <svg width="0" height="0" style="position:absolute">
    <defs>
      <symbol id="tab" viewBox="0 0 48 38">
        <path d="M0 0H40L48 38H0Z" fill="#1e88c8"/>
        <circle cx="20" cy="19" r="11" fill="none" stroke="#fff" stroke-width="1.6"/>
        <line x1="12.5" y1="26.5" x2="27.5" y2="11.5" stroke="#fff" stroke-width="1.6"/>
      </symbol>
    </defs>
  </svg>

  <div class="abs perk" style="left:346px;top:385px;width:176px"><svg width="48" height="38"><use href="#tab"/></svg><span>No salt required</span></div>
  <div class="abs perk" style="left:533px;top:385px;width:176px"><svg width="48" height="38"><use href="#tab"/></svg><span>No back washing<br>required</span></div>
  <div class="abs perk" style="left:346px;top:442px;width:176px"><svg width="48" height="38"><use href="#tab"/></svg><span>No regeneration<br>cycle required</span></div>
  <div class="abs perk" style="left:533px;top:442px;width:176px"><svg width="48" height="38"><use href="#tab"/></svg><span>No chemical or salt<br>added to the water</span></div>
  <div class="abs perk" style="left:346px;top:500px;width:176px"><svg width="48" height="38"><use href="#tab"/></svg><span>Maintenance free<br>media*</span></div>
  <div class="abs perk" style="left:533px;top:500px;width:176px"><svg width="48" height="38"><use href="#tab"/></svg><span>No electrical<br>connections</span></div>
  <div class="abs perk" style="left:346px;top:560px;width:176px"><svg width="48" height="38"><use href="#tab"/></svg><span>No drain connections</span></div>
  <div class="abs perk" style="left:533px;top:560px;width:176px"><svg width="48" height="38"><use href="#tab"/></svg><span>No control valves</span></div>
  <div class="abs perk" style="left:346px;top:622px;width:176px"><svg width="48" height="38"><use href="#tab"/></svg><span>No down time due to<br>clogged lines or pumps</span></div>
  <div class="abs perk" style="left:533px;top:622px;width:176px"><svg width="48" height="38"><use href="#tab"/></svg><span>Increases the life of<br>your RO membrane</span></div>
  <div class="abs perk wide" style="left:346px;top:681px;width:358px"><svg width="48" height="38"><use href="#tab"/></svg><span>Eliminates existing scale in water lines and equipment</span></div>

  <div class="abs results">
    <div class="result" style="left:12px" role="img" aria-label="Photo of scale buildup inside a brewer tank"></div>
    <div class="result" style="left:180px" role="img" aria-label="Photo of a clean brewer tank after treatment"></div>
    <div class="caption" style="left:6px">Scale buildup in a 5 gallon brewer<br>before Brivora Water Systems</div>
    <div class="caption" style="left:174px">5 Gallon Brewer 2 weeks<br>after Brivora Water Systems</div>
  </div>

  <div class="abs footer-dark"></div>
  <svg class="abs" style="left:0;top:973px" width="734" height="65">
    <path d="M0 0H150L180 65H0Z" fill="#1e88c8"/>
    <path d="M545 11H734V65H570Z" fill="#fff"/>
  </svg>
  <div class="abs contact-now">CONTACT US NOW</div>
  <div class="abs phone">
    <svg width="18" height="18" viewBox="0 0 24 24"><path d="M6 2l4 5-2 3c1 3 3 5 6 6l3-2 5 4-2 4C11 21 3 13 2 4z" fill="none" stroke="#3aa6e6" stroke-width="2"/></svg>
    (480) 555-0162
  </div>
  <div class="abs mail">
    <svg width="20" height="16" viewBox="0 0 24 18"><rect x="1" y="1" width="22" height="16" fill="none" stroke="#3aa6e6" stroke-width="2"/><path d="M1 1l11 9 11-9" fill="none" stroke="#3aa6e6" stroke-width="2"/></svg>
    @Your mail.com
  </div>
  <div class="abs states">ARIZONA • CALIFORNIA<br>MICHIGAN • NEVADA • UTAH</div>
</main>
</body>
</html>
```